Design a beautiful book cover for my self help book

The Craft of Hush is a book I've written about how I learnt to quite my mind, rid myself of old pain and stand in my intuition. It's one simple practical tool to find you moment and step into your abundance. We need a cover that reflects this amazing concept! The current cover is attached. It's too dark and not in tune with the market. Please search books with similar content and make design similar yet different.

Target Market(s)

People into self help or motivational content. As well as people suffering from depression, stress, anxiety etc.

Industry/Entity Type

Self Help

Requirements
Must have
• A light airy feel of freedom
Nice to have
• Some sort of linage from current cover
Should not have
• Dark, ambiguous,

```html
<!DOCTYPE html>
<html lang="en">
<head>
<meta charset="UTF-8">
<title>The Craft of Hush — Book Cover</title>
<link href="https://fonts.googleapis.com/css2?family=Oswald:wght@300&family=Montserrat:wght@500;700&family=Allura&display=swap" rel="stylesheet">
<style>
  :root {
    --backdrop: #2a2621;
    --sky-deep: #2fa9d6;
    --sky-mid: #4cbde4;
    --sky-low: #5aa9ea;
    --glow: #ffffff;
    --ink: #0d0d0d;
    --tagline: #ffffff;
  }
  html, body {
    margin: 0;
    padding: 0;
    width: 1200px;
    height: 857px;
    overflow: hidden;
    background: var(--backdrop);
  }
  .canvas {
    position: relative;
    width: 1200px;
    height: 857px;
  }
  .book-cover {
    position: absolute;
    left: 369px;
    top: 81px;
    width: 463px;
    height: 694px;
    overflow: hidden;
    background: linear-gradient(180deg, var(--sky-mid) 0%, var(--sky-deep) 45%, #4fb3e6 80%, var(--sky-low) 100%);
    box-shadow: 0 10px 30px rgba(0,0,0,0.45);
  }
  .light-glow {
    position: absolute;
    inset: 0;
    background:
      radial-gradient(ellipse 46% 40% at 50% 55%, var(--glow) 0%, rgba(255,255,255,0.9) 16%, rgba(214,242,252,0.7) 38%, rgba(160,220,243,0.3) 65%, rgba(160,220,243,0) 100%);
  }
  .tagline {
    position: absolute;
    top: 70px;
    left: 0;
    width: 100%;
    margin: 0;
    text-align: center;
    font-family: "Montserrat", sans-serif;
    font-weight: 500;
    font-size: 22px;
    line-height: 28px;
    color: var(--tagline);
  }
  .title {
    margin: 0;
    font-weight: normal;
    color: var(--ink);
  }
  .title-lead,
  .title-word {
    position: absolute;
    left: 0;
    width: 100%;
    text-align: center;
  }
  .title-lead {
    top: 236px;
    font-family: "Oswald", sans-serif;
    font-weight: 300;
    font-size: 64px;
    line-height: 76px;
    letter-spacing: 0.03em;
  }
  .title-word {
    top: 318px;
    font-family: "Allura", cursive;
    font-size: 112px;
    line-height: 130px;
  }
  .author {
    position: absolute;
    top: 622px;
    left: 0;
    width: 100%;
    margin: 0;
    text-align: center;
    font-family: "Montserrat", sans-serif;
    font-weight: 700;
    font-size: 24px;
    line-height: 30px;
    letter-spacing: 0.22em;
    color: var(--ink);
  }
</style>
</head>
<body>
<main class="canvas">
  <section class="book-cover">
    <div class="light-glow" role="img" aria-label="Radiant burst of white light at the centre of a blue sky"></div>
    <p class="tagline">Do you think too much?</p>
    <h1 class="title">
      <span class="title-lead">THE CRAFT OF</span>
      <span class="title-word">Hush</span>
    </h1>
    <p class="author">COREY FLINT</p>
  </section>
</main>
</body>
</html>
```